Melissa Dorvan Personal Business Card

I like orange. It's would better if my card have an orange background
Address: 5820 Halvers Lane #417
San Jose
California
US
Tel: 4085172049

Industry/Entity Type

Business

```html
<!DOCTYPE html>
<html lang="en">
<head>
<meta charset="utf-8">
<title>Melissa Dorvan – Business Card Options</title>
<link rel="stylesheet" href="https://fonts.googleapis.com/css2?family=Jost:wght@400&family=Russo+One&family=Arimo:wght@400&display=swap">
<style>
  :root {
    --backdrop: #dddddd;
    --card-orange: #f57f20;
    --card-ink: #ffffff;
  }
  * { margin: 0; padding: 0; box-sizing: border-box; }
  html, body {
    width: 1200px;
    height: 840px;
    overflow: hidden;
    background: var(--backdrop);
  }
  .canvas {
    position: relative;
    width: 1200px;
    height: 840px;
  }
  .card {
    position: absolute;
    width: 478px;
    height: 272px;
    background: var(--card-orange);
    color: var(--card-ink);
  }

  /* Option 1: centered with divider rule */
  .card--ruled { left: 124px; top: 142px; font-family: "Jost", sans-serif; }
  .card--ruled .phone {
    position: absolute; top: 98px; left: 0; width: 100%;
    text-align: center; font-size: 22px; letter-spacing: 0.3px;
  }
  .card--ruled .divider {
    position: absolute; top: 139px; left: 55px; width: 370px; height: 2px;
    background: var(--card-ink);
  }
  .card--ruled .address {
    position: absolute; top: 151px; left: 0; width: 100%;
    text-align: center; font-size: 15px; letter-spacing: 0.2px;
  }

  /* Option 2: bold headline phone */
  .card--headline { left: 661px; top: 142px; }
  .card--headline .phone {
    position: absolute; top: 112px; left: 0; width: 100%;
    text-align: center; font-family: "Russo One", sans-serif;
    font-size: 32px; letter-spacing: 1px;
  }
  .card--headline .address {
    position: absolute; top: 224px; left: 0; width: 100%;
    text-align: center; font-family: "Jost", sans-serif;
    font-size: 15px; letter-spacing: 0.2px;
  }

  /* Option 3: stacked corner block */
  .card--stacked { left: 384px; top: 460px; font-family: "Arimo", sans-serif; }
  .card--stacked .contact-block {
    position: absolute; left: 34px; top: 194px;
    font-size: 14px; line-height: 18px;
  }
</style>
</head>
<body>
<main class="canvas">
  <section class="card card--ruled">
    <p class="phone">+(408) 517 2049</p>
    <div class="divider"></div>
    <p class="address">5820 Halvers Lane #417, San Jose, California, US</p>
  </section>

  <section class="card card--headline">
    <p class="phone">+(408) 517 2049</p>
    <p class="address">5820 Halvers Lane #417, San Jose, California, US</p>
  </section>

  <section class="card card--stacked">
    <div class="contact-block">
      <p class="phone">+(408) 517 2049</p>
      <p class="street">5820 Halvers Lane #417</p>
      <p class="city">San Jose, California, US</p>
    </div>
  </section>
</main>
</body>
</html>
```